SEO and image area for top of invitation website

We need to add an area on our final category pages for SEO text. Instead of just adding text, we'd like to develop a graphical approach that keeps with our soft, feminine look.

You can view an example of our current final category page at http://www.cardmeadow.example/invitations/boy-birthday

I've attached an image of what we're thinking it could look like, but you're welcome to alter the design.

The area should be the same width as our site, but can be any height you determine appropriate.

The winner of this project may be approached to develop the additional designs and backgrounds for us as another project. We additionally have several other projects we're interested in doing with the winner.
Updates

We have had a question about the right side of the banner, and what "Free Unlimited Proofs" mean.

About Free Unlimited Proofs:

We are a custom invitation printing company. When a customer orders an invitation from us, they tell us what information we want on the invitation. We then create an electronic sample, or "proof", of what it will look like. We then email it to the customer and they can tell us if they want to make any more changes. We will continue to send them samples, or what we call "proofs", until they are completely satisfied with the way it looks.

We offer Free UNLIMITED Proofs. Compared to our competitors, we are the only one to offer free unlimited proofs.

So, for the right side of this banner, we need an image, or a badge, promoting that we offer free unlimited proofs, and you can include that we are the only ones to do it, if your design has space for that information.

Also, keep in mind, that for other category pages, we may create different images or badges to put in this area - such as for our Low Price Guarantee or to promote a coupon or specific product, for example. So, your design should be able to work with various images on the right side.

Target Market(s)

Our demographic is 100% women, ages 25-60.

Industry/Entity Type

Seo

Requirements
Must have
• The area must have 3 things:
1) Area for the title of the page.
2) Area for SEO text describing the category page.
3) Area for an image. Keep in mind that this image may change for each category page. For this project, you will create an image for our offering of "Free Unlimited Proofs". On other pages, we may display other images we create such as "Low Price Guarantee" or images of certain products we'd like to promote. Just keep this in mind when you're making the design flow.
Nice to have
• Optional: Light design background. We wouldn't mind there being a slight graphical background to this area, to keep it interesting to the eye. Then, for other category pages, we may make additional backgrounds to use in this box area.

```html
<!DOCTYPE html>
<html lang="en">
<head>
<meta charset="utf-8">
<title>Boy Birthday Invitations · Card Meadow</title>
<link rel="stylesheet" href="https://fonts.googleapis.com/css2?family=Bitter:wght@400;700&family=Open+Sans:wght@400;600;700&display=swap">
<style>
:root{
  --ink:#5f5a5c;
  --teal:#1ea59a;
  --teal-bright:#2cb5a0;
  --line:#d9d6d6;
  --bar:#f4f3f3;
  --card-bg:#f1efef;
  --card-border:#cfcccc;
  --yellow:#f6cf2e;
  --yellow-dark:#e2b414;
  --badge-brown:#5b4a4e;
}
*{box-sizing:border-box;margin:0;padding:0}
html,body{width:1200px;height:855px;overflow:hidden;background:#fff}
.canvas{position:relative;width:1200px;height:855px;overflow:hidden}
.page{position:absolute;left:0;top:0;width:1400px;height:998px;overflow:hidden;transform:scale(0.857143);transform-origin:0 0;font-family:'Bitter',Georgia,serif;color:var(--ink)}
.abs{position:absolute}

/* utility bar */
.utility-bar{left:0;top:0;width:1400px;height:28px;background:var(--bar);border-bottom:1px solid #e4e2e2;font-family:'Open Sans',Arial,sans-serif;font-size:11.7px;font-weight:700;color:#555;white-space:nowrap}
.utility-item{position:absolute;top:0;height:28px;display:flex;align-items:center;gap:7px}
.utility-sep{position:absolute;top:0;width:1px;height:28px;background:#ddd}

/* header */
.logo-mark{left:216px;top:46px;width:64px;height:66px;background:#e7e4e4;border-radius:4px}
.logo-name{left:290px;top:60px;font-size:41px;font-weight:400;color:#6b5b5f;letter-spacing:-.5px;white-space:nowrap}
.search{left:571px;top:66px;width:290px;height:48px;background:#f2f1f1;border:1px solid #e1dfdf;border-radius:4px}
.search-field{position:absolute;left:6px;top:6px;width:216px;height:34px;background:#fff;border:1px solid #e6e4e4}
.search-btn{position:absolute;left:223px;top:7px;width:60px;height:32px;background:#bdbbbb;border-radius:3px;color:#fff;font-size:13px;display:flex;align-items:center;justify-content:center}
.account{top:80px;font-family:'Open Sans',Arial,sans-serif;font-size:12.5px;letter-spacing:.4px;color:#444;white-space:nowrap}
.cart-count{left:1091px;top:77px;font-family:'Open Sans',Arial,sans-serif;font-size:16px;color:#555}

/* main nav */
.main-nav{left:212px;top:141px;width:960px;height:48px;border-top:1px solid var(--line);border-bottom:1px solid var(--line)}
.main-nav span{position:absolute;top:11px;font-size:19px;color:#6a6466;white-space:nowrap}

.breadcrumb{left:212px;top:208px;font-size:12.5px;color:#555;white-space:nowrap}
.breadcrumb a{color:var(--teal);text-decoration:none}

/* category banner */
.category-banner{left:212px;top:239px;width:706px;height:200px;background:linear-gradient(90deg,#ffffff 0%,#fbfaf5 55%,#f3f6ea 100%);overflow:hidden}
.banner-art{position:absolute}
.banner-title{position:absolute;left:78px;top:24px;font-size:31px;color:var(--teal-bright);font-weight:400;white-space:nowrap}
.banner-copy{position:absolute;left:79px;top:72px;width:530px;font-size:13.3px;line-height:15.6px;color:#6d6769}

.proofs-badge{left:922px;top:239px;width:250px;height:200px;background:linear-gradient(160deg,#34bc9f,#1f9e8e);overflow:hidden}
.proofs-art{position:absolute;right:0;top:0;width:90px;height:200px;background:linear-gradient(180deg,#e8f3f1,#3a8cc9 60%,#2f6f9d)}
.proofs-text{position:absolute;left:20px;top:22px;color:#fff;line-height:1}
.proofs-text .big{font-size:42px;font-weight:700}
.proofs-text .mid{font-size:24px;font-weight:400;display:block;margin-top:3px}
.proofs-text .mid.bold{font-weight:700}
.proofs-tag{position:absolute;left:20px;top:148px;color:#fff;font-size:17px;line-height:19px;white-space:nowrap}
.proofs-tag b{font-weight:700}

/* sort & pager */
.sort{left:227px;top:458px;font-size:16px;color:#666}
.sort-opt{top:461px;font-size:13px;color:#555}
.pager{left:972px;top:457px;display:flex;align-items:center;font-size:13px;color:var(--teal)}
.pager .num{width:16.6px;text-align:center}
.pager .num.current{color:#666}
.pager .arrow{width:22px;height:22px;border-radius:50%;display:flex;align-items:center;justify-content:center}

/* filters */
.filter-head{left:222px;font-size:17px;color:#6a6466;display:flex;align-items:center;gap:8px;white-space:nowrap}
.filter-head::before{content:"";border-left:6px solid #777;border-top:5px solid transparent;border-bottom:5px solid transparent}
.color-row{left:238px;font-family:'Open Sans',Arial,sans-serif;font-size:12.5px;color:#555;display:flex;align-items:center;gap:8px}
.swatch{width:15px;height:15px;border-radius:50%;border:1px solid #ccc}
.all-colors{left:242px;top:832px;font-family:'Open Sans',Arial,sans-serif;font-size:12.5px;color:#555}
.filter-divider{left:212px;width:240px;height:3px;background:#dcdada}

/* product grid */
.product-card{width:222px;height:222px;background:var(--card-bg);border:1px solid var(--card-border);border-radius:2px}
.product-art{position:absolute}
.quick-view{position:absolute;bottom:-12px;left:50%;transform:translateX(-50%);width:96px;height:25px;border-radius:5px;background:linear-gradient(#fbdf5c,var(--yellow));border:1px solid var(--yellow-dark);font-family:'Open Sans',Arial,sans-serif;font-size:11.5px;font-weight:700;color:#4d4420;display:flex;align-items:center;justify-content:center}
</style>
</head>
<body>
<div class="canvas">
<div class="page">

  <div class="abs utility-bar">
    <div class="utility-item" style="left:228px">
      <svg width="18" height="14" viewBox="0 0 18 14"><rect x="0" y="2" width="11" height="8" fill="#666"/><path d="M11 5h4l3 3v2h-7z" fill="#666"/><circle cx="4" cy="11" r="2" fill="#666"/><circle cx="14" cy="11" r="2" fill="#666"/></svg>
      FREE SHIPPING on orders over $150 - no coupon needed!
    </div>
    <div class="utility-sep" style="left:594px"></div>
    <div class="utility-item" style="left:605px">
      <svg width="17" height="13" viewBox="0 0 17 13"><path d="M1 1h10v7H5l-3 3V8H1z" fill="#666"/><path d="M12 4h4v6h-1v2l-2-2H7V9h5z" fill="#888"/></svg>
      Live Help
    </div>
    <div class="utility-sep" style="left:697px"></div>
    <div class="utility-item" style="left:713px">
      <svg width="18" height="13" viewBox="0 0 18 13"><path d="M1 4c3-4 13-4 16 0l-1 2-3-1V3H5v2L2 6z" fill="#666"/><path d="M4 7h10l2 5H2z" fill="#666"/></svg>
      888.555.0142
    </div>
    <div class="utility-sep" style="left:832px"></div>
    <div class="utility-item" style="left:843px">
      <svg width="16" height="16" viewBox="0 0 16 16"><path d="M2 2h6l7 7-6 6-7-7z" fill="none" stroke="#666" stroke-width="2"/><circle cx="5.5" cy="5.5" r="1.3" fill="#666"/></svg>
      Become a Designer · Earn Commission
    </div>
  </div>

  <div class="abs logo-mark"></div>
  <div class="abs logo-name">Card Meadow</div>

  <div class="abs search">
    <div class="search-field"></div>
    <div class="search-btn">search</div>
  </div>
  <div class="abs account" style="left:884px">LOGIN</div>
  <div class="abs account" style="left:936px">CREATE ACCOUNT</div>
  <svg class="abs" style="left:1060px;top:78px" width="20" height="18" viewBox="0 0 20 18"><path d="M1 2h3l2 9h10l2-7H5" fill="none" stroke="#666" stroke-width="2"/><circle cx="8" cy="15" r="1.6" fill="#666"/><circle cx="15" cy="15" r="1.6" fill="#666"/></svg>
  <div class="abs cart-count">0</div>

  <nav class="abs main-nav">
    <span style="left:20px">Wedding</span>
    <span style="left:140px">Party</span>
    <span style="left:226px">Baby and Kids</span>
    <span style="left:387px">Holiday</span>
    <span style="left:494px">Graduation</span>
    <span style="left:634px">Business</span>
    <span style="left:749px">Stationery</span>
  </nav>

  <div class="abs breadcrumb"><a href="#">Party</a> · <a href="#">Kids Birthday Party Invitations</a> · Boy Birthday Invitations</div>

  <section class="abs category-banner">
    <div class="banner-art" role="img" aria-label="Striped candy cane decoration" style="left:2px;top:0;width:58px;height:38px;background:linear-gradient(135deg,#d84a3a,#f3efe6 50%,#3f9a4c);border-radius:0 0 40px 0;opacity:.8"></div>
    <div class="banner-art" role="img" aria-label="Illustrated toy soldier and teddy bear" style="left:0;top:122px;width:76px;height:78px;background:linear-gradient(180deg,#e8a25c,#b5462f);border-radius:38px 38px 0 0"></div>
    <div class="banner-art" role="img" aria-label="Illustrated toys: green crocodile, purple dinosaur, toy turtle and party confetti" style="left:618px;top:0;width:88px;height:200px;background:linear-gradient(180deg,rgba(143,207,74,.85) 0 30%,rgba(240,236,216,.6) 30% 58%,#b98a4a 58% 80%,#7a4a9a 80%)"></div>
    <h1 class="banner-title">Boy Birthday Invitations</h1>
    <p class="banner-copy">Lorem ipsum dolor sit amet, consectetur adipiscing elit. Proin vulputate massa ac mauris posuere in auctor nibh congue. Nullam luctus porttitor lacus, eget condimentum rutrum id. Duis est risus, porta eget luctus et, scelerisque sed lectus. In hac habitasse platea dictumst. Curabitur fringilla diam sit amet nibh tempus sit amet posuere sapien porta.</p>
  </section>

  <aside class="abs proofs-badge">
    <div class="proofs-art" role="img" aria-label="Fanned sample invitation cards"></div>
    <svg class="abs" style="left:0;top:0" width="145" height="140" viewBox="0 0 145 140"><path d="M0 0H130L142 32 125 60 140 95 112 122 0 140z" fill="var(--badge-brown)"/></svg>
    <div class="proofs-text"><span class="big">Free</span><span class="mid">Unlimited</span><span class="mid bold">Proofs</span></div>
    <div class="proofs-tag"><b>Only with</b><br>Card Meadow!</div>
  </aside>

  <div class="abs sort">Sort By:</div>
  <div class="abs sort-opt" style="left:301px">Price</div>
  <div class="abs sort-opt" style="left:350px">Name</div>
  <div class="abs sort-opt" style="left:404px">Vendor</div>

  <div class="abs pager">
    <span class="arrow" style="background:#cfcccc"><svg width="12" height="10" viewBox="0 0 12 10"><path d="M11 5H2M5 1 1 5l4 4" stroke="#fff" stroke-width="2" fill="none"/></svg></span>
    <span class="num current" style="margin-left:2px">1</span><span class="num">2</span><span class="num">3</span><span class="num">4</span><span class="num">5</span><span class="num">6</span><span class="num">7</span><span class="num">8</span><span class="num">9</span>
    <span class="arrow" style="background:var(--teal)"><svg width="12" height="10" viewBox="0 0 12 10"><path d="M1 5h9M7 1l4 4-4 4" stroke="#fff" stroke-width="2" fill="none"/></svg></span>
  </div>

  <div class="abs filter-head" style="top:519px">Filter By Color</div>
  <div class="abs color-row" style="top:551px"><span class="swatch" style="background:#333"></span>Black</div>
  <div class="abs color-row" style="top:571px"><span class="swatch" style="background:#5b8de0"></span>Blue</div>
  <div class="abs color-row" style="top:591px"><span class="swatch" style="background:#8c6651"></span>Brown</div>
  <div class="abs color-row" style="top:611px"><span class="swatch" style="background:#f0ad1c"></span>Gold</div>
  <div class="abs color-row" style="top:631px"><span class="swatch" style="background:#7bd47b"></span>Green</div>
  <div class="abs color-row" style="top:651px"><span class="swatch" style="background:#cfcfcf"></span>Grey</div>
  <div class="abs color-row" style="top:671px"><span class="swatch" style="background:#f7f3df"></span>Ivory</div>
  <div class="abs color-row" style="top:691px"><span class="swatch" style="background:#f6b26b"></span>Orange</div>
  <div class="abs color-row" style="top:711px"><span class="swatch" style="background:#f6b8e6"></span>Pink</div>
  <div class="abs color-row" style="top:731px"><span class="swatch" style="background:#7a2d76"></span>Purple</div>
  <div class="abs color-row" style="top:751px"><span class="swatch" style="background:#e4575a"></span>Red</div>
  <div class="abs color-row" style="top:771px"><span class="swatch" style="background:#fff"></span>Silver</div>
  <div class="abs color-row" style="top:791px"><span class="swatch" style="background:#fff"></span>White</div>
  <div class="abs color-row" style="top:811px"><span class="swatch" style="background:#f6ee6c"></span>Yellow</div>
  <div class="abs all-colors">ALL COLORS</div>
  <div class="abs filter-divider" style="top:855px"></div>
  <div class="abs filter-head" style="top:869px">Filter By Card Size</div>
  <div class="abs filter-divider" style="top:921px"></div>
  <div class="abs filter-head" style="top:935px">Filter By # of Photos</div>
  <div class="abs filter-divider" style="top:987px"></div>

  <div class="abs product-card" style="left:472px;top:510px">
    <div class="product-art" role="img" aria-label="Pirate party invitation with parrot, ship and child photo" style="left:29px;top:0;width:162px;height:220px;background:linear-gradient(180deg,#e03a2e 0 33%,#f19a2a 33% 66%,#3aa0d8 66%)"></div>
    <div class="quick-view">Quick View</div>
  </div>
  <div class="abs product-card" style="left:711px;top:510px">
    <div class="product-art" role="img" aria-label="Birthday invitation with child photo on a starry border" style="left:29px;top:0;width:162px;height:220px;background:linear-gradient(180deg,#6ea84a 0 48%,#2d9fd9 48% 62%,#f39c2a 62%)"></div>
    <div class="quick-view">Quick View</div>
  </div>
  <div class="abs product-card" style="left:950px;top:510px">
    <div class="product-art" role="img" aria-label="Orange dinosaur-shaped birthday invitation" style="left:4px;top:6px;width:214px;height:130px;background:radial-gradient(ellipse at 55% 55%,#f7b31e 0 55%,transparent 56%)"></div>
    <div class="quick-view">Quick View</div>
  </div>

  <div class="abs product-card" style="left:472px;top:752px">
    <div class="product-art" role="img" aria-label="Bowling strike birthday invitation" style="left:62px;top:0;width:96px;height:220px;background:linear-gradient(180deg,#d9302a 0 20%,#3aa3e0 20%)"></div>
    <div class="quick-view">Quick View</div>
  </div>
  <div class="abs product-card" style="left:711px;top:752px">
    <div class="product-art" role="img" aria-label="Water slide birthday invitation with child sliding" style="left:2px;top:0;width:216px;height:137px;background:linear-gradient(135deg,#a8d85a 0 45%,#f4c23a 45% 60%,#e0462e 60% 72%,#a8d85a 72%)"></div>
    <div class="quick-view">Quick View</div>
  </div>
  <div class="abs product-card" style="left:950px;top:752px">
    <div class="product-art" role="img" aria-label="Space alien birthday invitation with flying saucer" style="left:2px;top:0;width:216px;height:137px;background:linear-gradient(180deg,#3ab2e8,#1e8fd0)"></div>
    <div class="quick-view">Quick View</div>
  </div>

  <div class="abs product-card" style="left:472px;top:994px"></div>
  <div class="abs product-card" style="left:711px;top:994px"></div>
  <div class="abs product-card" style="left:950px;top:994px"></div>

</div>
</div>
</body>
</html>
```